Energy cost saving website (job description rewritten!)

Job Type: WordPress design
Task Outline: Create a WordPress design
Task Description:
We are new business (Germany) in the market of saving costs by power-saving (name: 'uns-gefaellt-der-Ruhetag.de'). This is reached by changing the supplier, the use of LED bulbs, energy saving washing machines, stoves, microwaves, hairdryers, vacuum cleaners and the like - where all of these be selled or affiliated through the website maybe you will create for us.
Design parameters:
We want a serious design that embodies a feeling of honesty, competence and capability.
Visitors should particularly see that this site saves them money!
The home page mainly should act as a selector of possibilities saving money by power-saving, usage of LED bulbs and large energy saving household devices (washing machines, etc.)
Updates
Hello designers,
browsing through the PixelHarbors files of portfolios I found one header graphics which excites me. Please find it here: http://www.pixelharbor-example.com/design/482613/wordpress-design-by-tarun-mehlvi . Note: it is NOT the picture but the shadowing. So if you consider this in your concepts would be another 'nice-to-have'.
Thanks.
Reason: Give more time for newly invited disigners to submit designs.
Reason: Some designs still unter contruction.
Target Market(s)
People looking out for saving money by power-saving.
Industry/Entity Type
Business
Requirements
Must have
- Look and feel of 'this site saves me money'!
Nice to have
- We love 3D effects, but its not a must have. We also like cartoons, but feel free to develop your own concept, please. An appropriate backgrond picture would be nice.
Should not have
- Some kind of these exaggerated smiling or handshaking photos. That bathetic symbols like money bills or coins stacks.

```html
<!DOCTYPE html>
<html lang="en">
<head>
<meta charset="utf-8">
<title>LuxWatt GMBH – Energy Savings</title>
<link rel="stylesheet" href="https://fonts.googleapis.com/css2?family=Arimo:ital,wght@0,400;0,700;1,400;1,700&family=Jura:wght@400;600&family=Gelasio:ital@1&display=swap">
<style>
:root{
  --header-bg:#efe8a0;
  --nav-bg:#d5c963;
  --nav-text:#6a6322;
  --hero-bg:#fdf07c;
  --login-bg:#ececec;
  --input-bg:#8b8b8b;
  --olive:#6a6a1c;
  --footer-bg:#6a6434;
  --body-text:#6d6d6d;
  --heading:#2b2b2b;
  --accent-italic:#a69a3e;
  --red:#c0392b;
}
*{box-sizing:border-box;margin:0;padding:0}
html,body{width:1108px;height:1200px;overflow:hidden}
body{font-family:"Arimo",Arial,sans-serif;background:#fff;position:relative;color:var(--body-text)}
.abs{position:absolute;white-space:nowrap}
p.abs,.quote{white-space:normal}

/* header */
.site-header{left:0;top:0;width:1108px;height:77px;background:var(--header-bg);border-bottom:2px solid #f7f3c8}
.brand{left:82px;top:22px;font-family:"Jura",sans-serif;font-size:29px;color:#8c8228;font-weight:400;letter-spacing:.5px}
.search{left:618px;top:28px;width:205px;height:30px;background:#f5efab;border:1px solid #e4dc8c;font-size:12px;color:#8a8450;padding:9px 8px}
.search svg{position:absolute;right:7px;top:7px}
.call{left:845px;top:36px;font-size:13.5px;color:#333}

/* nav */
.main-nav{left:0;top:78px;width:1108px;height:47px;background:var(--nav-bg);box-shadow:0 2px 3px rgba(0,0,0,.15)}
.main-nav ul{list-style:none}
.main-nav li{position:absolute;top:12px;white-space:nowrap;font-family:"Jura",sans-serif;font-size:19px;line-height:22px;color:var(--nav-text);font-weight:600;letter-spacing:-.2px}

/* hero */
.hero{left:0;top:125px;width:1108px;height:341px;background:var(--hero-bg)}
.band{left:0;top:466px;width:1108px;height:114px;background:var(--login-bg)}
.slide{left:81px;top:159px;width:595px;height:322px;background:radial-gradient(ellipse at 55% 45%,#e9edf2 0%,#9aa4b0 45%,#2c2f34 100%);box-shadow:0 8px 10px -4px rgba(0,0,0,.45)}
.slider-dots{left:124px;top:447px;width:201px;height:34px;background:#1d1d1d;border-radius:6px 6px 0 0;display:flex;gap:16px;padding:10px 0 0 21px}
.slider-dots span{width:13px;height:13px;border-radius:50%;background:#444;box-shadow:inset 0 1px 2px #000}
.slider-dots span.active{background:#e04b4b}
.hero-title{left:696px;top:191px;font-family:"Jura",sans-serif;font-size:19.5px;color:#1f1f1f;font-weight:600}
.hero-sub{left:696px;top:233px;font-family:"Jura",sans-serif;font-size:15.5px;font-style:italic;font-weight:400;color:#6a6322}
.hero-text{left:696px;top:276px;width:325px;font-size:13px;line-height:21px;color:#8a8346;text-align:justify}
.hero-rule{left:698px;top:407px;width:213px;border-top:1px solid #cfc46a}
.btn-soft{left:919px;top:393px;width:99px;height:29px;background:#f1e584;border-radius:6px;box-shadow:0 1px 3px rgba(0,0,0,.25);font-size:13px;color:#948b3d;text-align:center;line-height:29px}

/* login */
.field{top:515px;width:308px;height:38px;background:var(--input-bg);color:#f2f2f2;font-size:13.5px;padding:12px 18px;box-shadow:inset 2px 2px 3px rgba(0,0,0,.25)}
.btn-outline{top:516px;height:34px;border:2px solid #8c8c8c;font-family:"Jura",sans-serif;font-size:19px;color:var(--olive);text-align:center;line-height:30px;font-weight:600;background:#f4f4f4}

/* products */
.section-title{font-size:16px;font-weight:700;color:var(--heading)}
.copy{font-size:12px;line-height:17px;color:var(--body-text);text-align:justify}
.carousel{left:394px;top:615px;width:623px;height:155px;background:#f4f4f4;border-radius:3px;box-shadow:0 1px 3px rgba(0,0,0,.2)}
.thumb{top:636px;width:177px;height:110px;border:1px solid #d7d7d7;border-radius:4px}
.arrow{top:680px}
.divider{left:82px;top:798px;width:944px;border-top:1px solid #e6e6e6}

.tagline{font-family:"Gelasio",serif;font-style:italic;font-size:13px;color:var(--accent-italic)}
.rule{top:1006px;border-top:1px solid #d5d5d5}
.btn-small{top:994px;height:26px;border:1px solid #9a9a9a;font-size:12px;color:#555;text-align:center;line-height:24px;background:#fff}
.avatar{left:583px;top:872px;width:68px;height:86px;background:linear-gradient(#5c6b7c,#2a3038);border-radius:30px 30px 6px 6px}
.client-name{left:563px;top:966px;font-size:12px;color:var(--red)}
.quote{left:691px;top:878px;width:326px;height:107px;border:1px solid #dcdcdc;border-radius:5px;padding:12px 10px;font-size:12px;line-height:17.5px;color:#6a6a6a}
.quote b{font-style:italic;color:#555}
.quote::before{content:"";position:absolute;left:-8px;top:26px;width:13px;height:13px;background:#fff;border-left:1px solid #dcdcdc;border-bottom:1px solid #dcdcdc;transform:rotate(45deg)}

/* footer */
.site-footer{left:0;top:1058px;width:1108px;height:142px;background:var(--footer-bg);border-top:2px dashed #8c8752;outline:4px solid #5f5a2d;outline-offset:-4px}
.footer-nav{left:82px;top:1094px;display:flex;gap:16px;font-size:12px;color:#f1efe0}
.copyright{left:81px;top:1128px;font-size:12px;color:#f1efe0}
.news-title{left:777px;top:1092px;font-size:16px;font-weight:700;color:#f1efe0;text-shadow:0 1px 1px rgba(0,0,0,.5)}
.news-input{left:740px;top:1121px;width:257px;height:27px;background:#2f302d;border:1px solid #4a4a3a;border-radius:2px;font-size:12px;color:#9c9c9c;padding:6px 9px}
.news-btn{left:740px;top:1160px;width:78px;height:28px;background:#fff;border:1px solid #ccc;border-radius:3px;font-size:12px;color:#222;text-align:center;line-height:26px}
</style>
</head>
<body>

<header class="abs site-header"></header>
<div class="abs brand">LuxWatt GMBH</div>
<div class="abs search">Search
  <svg width="18" height="16" viewBox="0 0 18 16"><circle cx="6" cy="6" r="4.5" fill="none" stroke="#333" stroke-width="2"/><line x1="9.5" y1="9" x2="16" y2="14" stroke="#333" stroke-width="3"/></svg>
</div>
<div class="abs call">Call Us On: 030-555-01842</div>

<nav class="abs main-nav">
  <ul>
    <li style="left:144px">Home</li>
    <li style="left:228px">About Us</li>
    <li style="left:334px">Products</li>
    <li style="left:443px">Cost Cutting</li>
    <li style="left:577px">Testimonials</li>
    <li style="left:722px">Latest News</li>
    <li style="left:857px">Contact Us</li>
  </ul>
</nav>

<section class="abs hero"></section>
<section class="abs band"></section>
<div class="abs slide" role="img" aria-label="Photo of a light bulb lying on an electricity statement"></div>
<div class="abs slider-dots"><span class="active"></span><span></span><span></span><span></span><span></span><span></span></div>
<h1 class="abs hero-title">The standard Lorem Ipsum passage</h1>
<h2 class="abs hero-sub">The standard Lorem Ipsum passage</h2>
<p class="abs hero-text">Lorem ipsum dolor sit amet, consectetur adipisicing elit, sed do eiusmod tempor incididunt ut labore et dolore magna aliqua. Ut enim ad minim veniam, quis nostrud exercitation ullamco laboris nisi ut aliquip ex ea commodo consequat.</p>
<div class="abs hero-rule"></div>
<div class="abs btn-soft">Read More</div>

<div class="abs field" style="left:123px">Email Id / Username</div>
<div class="abs field" style="left:455px">Password</div>
<div class="abs btn-outline" style="left:783px;width:87px">Login</div>
<div class="abs btn-outline" style="left:878px;width:101px">Register</div>

<h3 class="abs section-title" style="left:83px;top:620px">Our Products</h3>
<p class="abs copy" style="left:86px;top:654px;width:278px">Lorem ipsum dolor sit amet, consectetur adipisicing elit, sed do eiusmod tempor incididunt ut labore et dolore magna aliqua. Ut enim ad minim veniam, quis nostrud exercitation ullamco laboris nisi ut aliquip ex ea commodo consequat.</p>
<div class="abs carousel"></div>
<svg class="abs arrow" style="left:404px" width="12" height="16" viewBox="0 0 12 16"><path d="M9 2 L3 8 L9 14" fill="none" stroke="#111" stroke-width="3"/></svg>
<svg class="abs arrow" style="left:994px" width="12" height="16" viewBox="0 0 12 16"><path d="M3 2 L9 8 L3 14" fill="none" stroke="#111" stroke-width="3"/></svg>
<div class="abs thumb" style="left:423px;background:linear-gradient(90deg,#f2f2f2,#d8d6c8 50%,#f4f4f4)" role="img" aria-label="Product photo of LED and energy saving light bulbs"></div>
<div class="abs thumb" style="left:616px;background:radial-gradient(circle at 45% 55%,#d9403c 0%,#e8b0ae 35%,#f7f7f7 65%)" role="img" aria-label="Product photo of a red vacuum cleaner"></div>
<div class="abs thumb" style="left:808px;background:linear-gradient(135deg,#e6e6e6,#c4c4c4 50%,#8a8a8a)" role="img" aria-label="Product photo of white household appliances"></div>
<div class="abs divider"></div>

<h3 class="abs section-title" style="left:83px;top:825px">About Us</h3>
<div class="abs tagline" style="left:82px;top:845px">See what we do here</div>
<p class="abs copy" style="left:84px;top:875px;width:410px;line-height:18px">Lorem ipsum dolor sit amet, consectetur adipisicing elit, sed do eiusmod tempor incididunt ut labore et dolore magna aliqua. Ut enim ad minim veniam, quis nostrud exercitation ullamco laboris nisi ut aliquip ex ea commodo consequat. Duis aute irure dolor in reprehenderit in voluptate velit esse cillum dolore eu fugiat nulla pariatur. Excepteur sint occaecat cupidatat non proident, sunt in culpa qui officia deserunt mollit anim id est laborum</p>
<div class="abs rule" style="left:83px;width:311px"></div>
<div class="abs btn-small" style="left:410px;width:82px">Read More</div>

<h3 class="abs section-title" style="left:565px;top:825px">What Clients Say</h3>
<div class="abs tagline" style="left:564px;top:845px">Clients' say about us</div>
<div class="abs avatar" role="img" aria-label="Client portrait icon"></div>
<div class="abs client-name">Name, Designation</div>
<div class="abs quote"><b>Lorem ipsum dolor sit amet,</b> consectetur adipisicing elit, sed do eiusmod tempor incididunt ut labore et dolore magna aliqua. Ut enim ad minim veniam, quis nostrud exercitation ullamco laboris nisi ut aliquip ex</div>
<div class="abs rule" style="left:605px;width:310px"></div>
<div class="abs btn-small" style="left:931px;width:82px">View More</div>

<footer class="abs site-footer"></footer>
<div class="abs footer-nav"><span>Home</span><span>About Us</span><span>Products</span><span>Cost Cutting</span><span>Testimonials</span><span>Latest News</span><span>Contact Us</span></div>
<div class="abs copyright">Copyright</div>
<svg class="abs" style="left:740px;top:1090px" width="30" height="22" viewBox="0 0 30 22"><rect x="1" y="2" width="26" height="17" fill="#f1efe0" stroke="#999"/><path d="M1 2 L14 12 L27 2" fill="none" stroke="#999"/><path d="M18 15 H26 M23 12 L27 15 L23 18" fill="none" stroke="#6ab03c" stroke-width="2"/></svg>
<div class="abs news-title">Newsletter Signup</div>
<div class="abs news-input">E-mail Address</div>
<div class="abs news-btn">Subscribe</div>

</body>
</html>
```